design a construction company business card

Design business card around our logo. Card must have all the typical info: name, title, address, phone, email, business name, etc. Somewhere on the card I would like to see our motto "Built on integrity... Inspired by commitment." Consider adding a splash of bright orange to the card to complement the blues and silvers/grays in the logo. We are open to metallic inks, textures, etc. We would like to see options on both light and dark backgrounds. The font in the logo is Euro Technic Extended Regular.

```html
<!DOCTYPE html>
<html lang="en">
<head>
<meta charset="UTF-8">
<title>Harlow Builders – Business Card Options</title>
<link rel="stylesheet" href="https://fonts.googleapis.com/css2?family=Montserrat:wght@300;400;500&family=Source+Sans+3:wght@400&display=swap">
<style>
  :root {
    --page: #ffffff;
    --ink: #111111;
    --card-light: #ffffff;
    --card-dark: #2b2a2c;
    --blue: #1f63c6;
    --steel: #8c8c8c;
    --orange: #f0821e;
    --orange-deep: #e9641a;
    --text-grey: #6c6c6c;
    --text-dark: #2a2a2a;
    --text-light: #f2f2f2;
  }
  * { box-sizing: border-box; margin: 0; padding: 0; }
  html, body { width: 1200px; height: 1000px; overflow: hidden; background: var(--page); }
  .sheet { position: relative; width: 1200px; height: 1000px; }

  .section-title {
    position: absolute; left: 40px;
    font-family: "Source Sans 3", sans-serif; font-weight: 400;
    font-size: 34px; letter-spacing: 0.5px; color: var(--ink);
  }
  .section-title.light { top: 36px; }
  .section-title.dark { top: 466px; }

  .card {
    position: absolute; width: 540px; height: 309px; overflow: hidden;
    box-shadow: 3px 4px 10px rgba(0,0,0,0.28);
    font-family: "Montserrat", sans-serif;
  }
  .card.is-light { background: var(--card-light); }
  .card.is-dark { background: var(--card-dark); }
  .card-art { position: absolute; inset: 0; width: 100%; height: 100%; }

  .pos-a { left: 40px; } .pos-b { left: 620px; }
  .row-1 { top: 100px; } .row-2 { top: 530px; }

  .blue { fill: var(--blue); }
  .steel { fill: var(--steel); }
  .orange { fill: var(--orange); }

  /* front */
  .holder-name {
    position: absolute; left: 140px; top: 84px;
    font-weight: 300; font-size: 40px; letter-spacing: 2px; line-height: 1;
  }
  .is-light .holder-name { color: var(--orange-deep); }
  .is-dark .holder-name { color: var(--text-light); }
  .holder-role {
    position: absolute; left: 142px; top: 130px;
    font-size: 10px; letter-spacing: 0.8px; color: var(--text-grey); text-transform: uppercase;
  }
  .contact-list { position: absolute; left: 280px; top: 190px; list-style: none; }
  .contact-list li {
    display: flex; align-items: flex-start; gap: 12px;
    font-size: 9.5px; line-height: 1.35; text-transform: uppercase; margin-bottom: 16px;
  }
  .is-light .contact-list li { color: var(--text-dark); }
  .is-dark .contact-list li { color: var(--text-light); }
  .contact-list svg { width: 16px; height: 16px; flex: none; fill: var(--orange); }

  /* back */
  .wordmark {
    position: absolute; left: 300px; top: 124px; width: 200px; text-align: center;
    color: var(--blue); font-weight: 500; line-height: 1;
  }
  .wordmark-name { display: block; font-size: 40px; letter-spacing: 2px; }
  .wordmark-sub { display: block; font-size: 10.5px; letter-spacing: 1.2px; margin-top: 6px; }
  .web-address {
    position: absolute; left: 300px; top: 206px; width: 200px; text-align: center;
    font-size: 10px; letter-spacing: 0.5px; color: #9a9a9a;
  }
  .motto {
    position: absolute; left: 135px; right: 20px; top: 283px;
    font-size: 12px; letter-spacing: 0.2px; text-transform: uppercase;
    color: var(--text-dark); text-align: right; white-space: nowrap;
  }
</style>
</head>
<body>
<main class="sheet">
  <h2 class="section-title light">LIGHT BACKGROUND</h2>

  <!-- light front -->
  <section class="card is-light pos-a row-1">
    <svg class="card-art" viewBox="0 0 540 309" aria-hidden="true">
      <rect x="430" y="0" width="110" height="60" fill="#e3e8f6"/>
      <rect x="500" y="60" width="40" height="20" fill="#fbe3cd"/>
      <rect class="blue" x="0" y="0" width="14" height="309"/>
      <rect class="blue" x="14" y="226" width="100" height="18"/>
      <rect class="steel" x="14" y="252" width="76" height="8"/>
      <rect class="orange" x="14" y="268" width="124" height="16"/>
    </svg>
    <h1 class="holder-name">HARLOW XXX</h1>
    <p class="holder-role">Project Manager</p>
    <ul class="contact-list">
      <li><svg viewBox="0 0 24 24"><path d="M6.6 10.8a15 15 0 0 0 6.6 6.6l2.2-2.2c.3-.3.7-.4 1-.2 1.1.4 2.3.6 3.6.6.6 0 1 .4 1 1V20c0 .6-.4 1-1 1C10.6 21 3 13.4 3 4c0-.6.4-1 1-1h3.5c.6 0 1 .4 1 1 0 1.3.2 2.5.6 3.6.1.3 0 .7-.2 1z"/></svg>+1 . 555 . 010 . XXXX</li>
      <li><svg viewBox="0 0 24 24"><path d="M2 5h20v2l-10 6L2 7z M2 9l10 6 10-6v10H2z"/></svg>harlow@harlowbuilders.com</li>
      <li><svg viewBox="0 0 24 24"><path d="M12 2a7 7 0 0 0-7 7c0 5 7 13 7 13s7-8 7-13a7 7 0 0 0-7-7zm0 9.5A2.5 2.5 0 1 1 12 6.5a2.5 2.5 0 0 1 0 5z"/></svg><span>Elm Street XXXXX<br>XXXXXX, XXX 40210</span></li>
    </ul>
  </section>

  <!-- light back -->
  <section class="card is-dark pos-b row-1">
    <svg class="card-art" viewBox="0 0 540 309" aria-hidden="true">
      <rect class="blue" x="0" y="0" width="14" height="272"/>
      <rect class="blue" x="14" y="96" width="196" height="22"/>
      <rect class="steel" x="14" y="126" width="150" height="8"/>
      <rect class="orange" x="14" y="142" width="230" height="14"/>
      <rect class="orange" x="0" y="272" width="540" height="37"/>
    </svg>
    <div class="wordmark"><span class="wordmark-name">HARLOW</span><span class="wordmark-sub">BUILDERS, INC.</span></div>
    <p class="web-address">www.xxxxxxxxx.com</p>
    <p class="motto">Grounded in trust · Driven by craft</p>
  </section>

  <h2 class="section-title dark">DARK BACKGROUND</h2>

  <!-- dark front -->
  <section class="card is-dark pos-a row-2">
    <svg class="card-art" viewBox="0 0 540 309" aria-hidden="true">
      <rect x="430" y="0" width="110" height="60" fill="#000" opacity="0.2"/>
      <rect x="500" y="60" width="40" height="20" fill="#6a4a33" opacity="0.45"/>
      <rect class="blue" x="0" y="0" width="14" height="309"/>
      <rect class="blue" x="14" y="226" width="100" height="18"/>
      <rect class="steel" x="14" y="252" width="76" height="8"/>
      <rect class="orange" x="14" y="268" width="124" height="16"/>
    </svg>
    <h1 class="holder-name">HARLOW XXX</h1>
    <p class="holder-role">Owner</p>
    <ul class="contact-list">
      <li><svg viewBox="0 0 24 24"><path d="M6.6 10.8a15 15 0 0 0 6.6 6.6l2.2-2.2c.3-.3.7-.4 1-.2 1.1.4 2.3.6 3.6.6.6 0 1 .4 1 1V20c0 .6-.4 1-1 1C10.6 21 3 13.4 3 4c0-.6.4-1 1-1h3.5c.6 0 1 .4 1 1 0 1.3.2 2.5.6 3.6.1.3 0 .7-.2 1z"/></svg>+1 . 555 . 010 . XXXX</li>
      <li><svg viewBox="0 0 24 24"><path d="M2 5h20v2l-10 6L2 7z M2 9l10 6 10-6v10H2z"/></svg>harlow@harlowbuilders.com</li>
      <li><svg viewBox="0 0 24 24"><path d="M12 2a7 7 0 0 0-7 7c0 5 7 13 7 13s7-8 7-13a7 7 0 0 0-7-7zm0 9.5A2.5 2.5 0 1 1 12 6.5a2.5 2.5 0 0 1 0 5z"/></svg><span>Elm Street XXXXX<br>XXXXXX, XXX 40210</span></li>
    </ul>
  </section>

  <!-- dark back -->
  <section class="card is-dark pos-b row-2">
    <svg class="card-art" viewBox="0 0 540 309" aria-hidden="true">
      <rect class="blue" x="0" y="0" width="14" height="272"/>
      <rect class="blue" x="14" y="96" width="196" height="22"/>
      <rect class="steel" x="14" y="126" width="150" height="8"/>
      <rect class="orange" x="14" y="142" width="230" height="14"/>
      <rect class="orange" x="0" y="272" width="540" height="37"/>
    </svg>
    <div class="wordmark"><span class="wordmark-name">HARLOW</span><span class="wordmark-sub">BUILDERS, INC.</span></div>
    <p class="web-address">www.xxxxxxxxx.com</p>
    <p class="motto">Grounded in trust · Driven by craft</p>
  </section>
</main>
</body>
</html>
```